International Patent Law Firm Needs a New Website Design

We are an international, German-based patent law firm and are in need for a new website design.

Our current (old-fashioned) website is

www.prtv.example

Our Corporate Identity features that we want to keep are as follows.

1. Our PRTV logo in blue color on white background.

2. The tent roof design of the Harlow Meadow Arena.

We attach our current PRTV presentation, which gives you an idea of who we are, what our business is and what distinguishes us.

The new website design should express that we provide very reliable, high-quality Intellectual Property services, including patent and trademark services worldwide.

On the one hand, it should professional, on the other it should look young.

The managing partners of our patent law firm are in their 30ies and their 40ies, which is comparably young for a patent law firm of our size. Our team comprises about 20 patent attorneys and altogether 45 people.

Websites of competitors that we like are as follows.

http://www.qzd.example
http://morwellhastings.example
http://www.dellow.example
http://www.rplaw.example (here we like the structure, rather than the design)

There are two features that all these websites have in common and that we also would like to have implemented in our new website design.

1. A clear and self-explaining main menu in the header.

For example:

HOME OUR FIRM WHAT WE DO WHO WE ARE OUR CLIENTS OUR FEES CONTACT US

2. At least on the main page: A background picture filling the entire screen and having an appealing graphic. Maybe the tent roof of the Harlow Meadow Arena?

Further points that we believe to be important are as follows:

1. Our new website should have a simple menu navigation (not as complicated as the current one). It should have two levels, namely the main page and the subpages, that are all directly accessible via the main page, so that all the content can be reached with two clicks.

2. On the WHO WE ARE subpage we like the solution that there is a list of the names of the patent attorneys in the left column, and upon clicking on a name the full profile of the patent attorney including a photograph of the partner will appear. We will have new photographs of our team prepared and supplied to you.

3. On the WHAT WE DO subpage we like the solution that there is a list of the headlines of our fields of activity, like PATENTS, and upon clicking on a headline a more detailed description of the respective field of activity will appear.

4. Our new website should contain less content than our current website. The text will be supplied by us.

5. What is also very important is that the design will be optimized for access by PCs, by tablets and by smart phones (responsive design).

6. We will need both English and German language versions of the website, including all the subpages. We will provide you with the updated text for all the pages.

Thanks very much in advance for your work and your suggestion.

Best regards,

Jonas Terholt (Partner)

Target Market(s)

Innovative and Patenting Firms worldwide, Innovators, Inventors, Potential new Employees

Industry/Entity Type

Lawyer

Number of Pages Required

5+ page

Font styles to use
Sans Serif

Colors
0555a3
0293ce

Requirements
Must have
• New appealing and modern website, self-explaining and easy menu structure
Nice to have
• Maybe some appealing design showing that we are constantly at the edge of the new technical development
Should not have
• May not look old-fashioned, no complicated menu

```html
<!DOCTYPE html>
<html lang="en">
<head>
<meta charset="utf-8">
<title>PRTV Patent Attorneys</title>
<link href="https://fonts.googleapis.com/css2?family=Raleway:wght@300;400;500;600;700&family=Open+Sans:wght@400;600;700&display=swap" rel="stylesheet">
<style>
:root{
  --brand-blue:#0555a3;
  --accent-blue:#0293ce;
  --logo-blue:#7ea3d2;
  --ink:#222;
  --muted:#777;
  --soft-bg:#efefef;
  --footer-bg:#6e6e6e;
  --white:#fff;
}
*{margin:0;padding:0;box-sizing:border-box}
html,body{width:1200px;height:2203px;overflow:hidden}
body{position:relative;background:var(--white);font-family:'Open Sans',sans-serif;color:var(--ink)}
.abs{position:absolute}
.center{text-align:center}

.site-header{position:absolute;left:0;top:0;width:1200px;height:109px;background:var(--white)}
.brand{position:absolute;left:0;width:1200px;top:22px;text-align:center;font-family:'Raleway',sans-serif;font-weight:400;font-size:48px;letter-spacing:10px;color:var(--logo-blue)}
.lang{position:absolute;top:72px;display:block;width:32px;height:20px}
.lang-de{left:940px}
.lang-en{left:980px}

.main-nav{position:absolute;left:0;top:109px;width:1200px;height:50px;background:var(--brand-blue)}
.main-nav a{position:absolute;top:0;height:50px;line-height:50px;color:var(--white);text-decoration:none;font-family:'Raleway',sans-serif;font-weight:600;font-size:14px;text-align:center;width:130px;margin-left:-65px}
.main-nav a.active{background:var(--accent-blue);width:124px;margin-left:-62px}

.hero{position:absolute;left:0;top:159px;width:1200px;height:493px;
  background:linear-gradient(180deg,#6f8a6b 0%,#5f8450 35%,#4d6f43 60%,#8fa08f 100%);
  clip-path:polygon(0 0,100% 0,100% 454px,50% 493px,0 454px)}
.hero-title{position:absolute;left:0;width:1200px;top:155px;text-align:center;font-family:'Raleway',sans-serif;font-weight:700;font-size:47px;color:var(--white);letter-spacing:.5px}
.hero-sub{position:absolute;left:0;width:1200px;top:213px;text-align:center;font-family:'Raleway',sans-serif;font-weight:500;font-size:28px;color:var(--white)}
.hero-btn{position:absolute;left:536px;top:270px;width:129px;height:35px;border:2px solid var(--white);color:var(--white);font-family:'Raleway',sans-serif;font-size:13px;font-weight:600;line-height:31px;text-align:center}
.hero-arrow{position:absolute;top:183px;width:20px;height:36px}

.welcome{position:absolute;left:0;top:600px;width:1200px;height:360px;background:linear-gradient(180deg,#f5f5f5,#e7e7e7);z-index:-1}
.welcome-title{position:absolute;left:0;width:1200px;top:710px;text-align:center;font-family:'Raleway',sans-serif;font-weight:400;font-size:29px;color:var(--ink)}
.welcome-rule{position:absolute;left:532px;top:755px;width:122px;height:2px;background:var(--ink)}
.welcome-lead{position:absolute;left:180px;width:840px;top:783px;text-align:center;font-size:13.5px;line-height:19px;color:#333}
.welcome-body{position:absolute;left:180px;width:840px;top:831px;text-align:center;font-size:12px;line-height:18px;color:#888}

.service{position:absolute;top:1005px;width:240px;margin-left:-120px;text-align:center}
.service-icon{display:block;margin:0 auto;width:95px;height:95px}
.service h3{margin-top:14px;font-family:'Raleway',sans-serif;font-weight:400;font-size:19px;color:var(--ink)}
.service p{margin-top:5px;font-size:10.5px;line-height:17.5px;color:#666}
.btn-outline{position:absolute;top:210px;left:70px;width:100px;height:30px;border:2px solid var(--accent-blue);color:var(--accent-blue);font-family:'Raleway',sans-serif;font-size:10px;font-weight:600;line-height:26px;text-align:center}

.team{position:absolute;left:0;top:1317px;width:1200px;height:363px;background:var(--brand-blue)}
.team-title{position:absolute;left:0;width:1200px;top:34px;text-align:center;font-family:'Raleway',sans-serif;font-weight:400;font-size:22px;color:var(--white)}
.member{position:absolute;top:84px;width:200px;margin-left:-100px;text-align:center;color:var(--white)}
.member-photo{display:block;margin:0 auto;width:140px;height:140px;border-radius:50%;border:3px solid var(--white);background:linear-gradient(180deg,#d9d9d9,#8b8b8b)}
.member h4{margin-top:10px;font-family:'Raleway',sans-serif;font-weight:500;font-size:14.5px}
.member p{margin-top:4px;font-size:10.5px;line-height:17px}
.member .more{display:block;margin-top:2px;font-family:'Raleway',sans-serif;font-weight:700;font-size:11px}
.team-divider{position:absolute;top:90px;width:1px;height:222px;background:rgba(255,255,255,.25)}

.news-title{position:absolute;left:183px;top:1725px;font-family:'Raleway',sans-serif;font-weight:400;font-size:28px;color:#333}
.see-all{position:absolute;left:958px;top:1741px;width:80px;height:23px;background:var(--brand-blue);color:var(--white);font-size:11px;line-height:23px;text-align:center}
.post{position:absolute;top:1780px;width:255px}
.post-image{display:block;width:255px;height:122px}
.post h4{margin-top:20px;font-family:'Open Sans',sans-serif;font-weight:400;font-size:15px;color:#333}
.post p{margin-top:5px;font-size:10.5px;line-height:18px;color:#777}
.post .more{display:block;margin-top:6px;font-family:'Raleway',sans-serif;font-weight:700;font-size:11px;color:var(--brand-blue)}

.site-footer{position:absolute;left:0;top:2070px;width:1200px;height:133px;background:var(--footer-bg);color:var(--white)}
.footer-nav{position:absolute;left:181px;top:33px;font-family:'Raleway',sans-serif;font-weight:700;font-size:11px}
.footer-nav span{margin-right:21px}
.copyright{position:absolute;left:181px;top:57px;font-size:10.5px;color:#a8a8a8}
.social{position:absolute;top:83px;width:28px;height:28px;border-radius:50%;background:var(--white)}
.address{position:absolute;right:183px;top:25px;text-align:right;font-size:10.5px;line-height:17px}
</style>
</head>
<body>

<header class="site-header">
  <div class="brand">prtv</div>
  <svg class="lang lang-de" viewBox="0 0 32 20" aria-label="Deutsch">
    <rect width="32" height="7" fill="#111"/><rect y="7" width="32" height="6" fill="#d00"/><rect y="13" width="32" height="7" fill="#fc0"/>
  </svg>
  <svg class="lang lang-en" viewBox="0 0 32 20" aria-label="English">
    <rect width="32" height="20" fill="#1f3a8a"/>
    <path d="M0 0L32 20M32 0L0 20" stroke="#fff" stroke-width="4"/>
    <path d="M0 0L32 20M32 0L0 20" stroke="#c8102e" stroke-width="1.5"/>
    <path d="M16 0V20M0 10H32" stroke="#fff" stroke-width="6"/>
    <path d="M16 0V20M0 10H32" stroke="#c8102e" stroke-width="3"/>
  </svg>
</header>

<nav class="main-nav">
  <a class="active" style="left:247px">HOME</a>
  <a style="left:393px">OUR FIRM</a>
  <a style="left:564px">WHAT WE DO</a>
  <a style="left:746px">OUR PEOPLE</a>
  <a style="left:925px">CONTACT US</a>
</nav>

<section class="hero" role="img" aria-label="Aerial view of Harlow Meadow Arena park with lake and tent roof">
  <svg class="hero-arrow" style="left:137px" viewBox="0 0 20 36"><path d="M16 4L4 18L16 32" fill="none" stroke="#fff" stroke-width="4"/></svg>
  <svg class="hero-arrow" style="left:1060px" viewBox="0 0 20 36"><path d="M4 4L16 18L4 32" fill="none" stroke="#fff" stroke-width="4"/></svg>
  <h1 class="hero-title">LEGAL SERVICE &amp; EXPERTISE</h1>
  <p class="hero-sub">MAECENAS ALIQUET VELIT TURPIS</p>
  <div class="hero-btn">LEARN MORE</div>
</section>

<div class="welcome" role="img" aria-label="Faded city skyline in the background"></div>
<h2 class="welcome-title">WELCOME TO PRTV</h2>
<div class="welcome-rule"></div>
<p class="welcome-lead">apibus malesuada fringilla eu condimentum quis tellus Aenean porttitor eros vel dolor Donec convallis pede venenatis nibh Duis quam Nam eget lacus Aliquam erat volutpat Quisque dignissim congue leo</p>
<p class="welcome-body">Mauris vel lacus vitae felis vestibulum volutpat imperdiet ac nisl Cum sociis natoque penatibus et magnis dis parturient montes nascetur ridiculus mus In iaculis facilisis massa Etiam eu urna Sed porta Suspendisse quam leo molestie sed luctus quis feugiat in pede Fusce tellus Sed metus augue convallis et vehicula ut pulvinar eu ante Integer orci tellus tristique vitae consequat nec</p>

<div class="service" style="left:316px">
  <svg class="service-icon" viewBox="0 0 95 95">
    <circle cx="47.5" cy="47.5" r="47.5" fill="var(--accent-blue)"/>
    <rect x="31" y="24" width="30" height="42" fill="none" stroke="#fff" stroke-width="2.5"/>
    <rect x="35" y="28" width="30" height="42" fill="none" stroke="#fff" stroke-width="1.5"/>
    <path d="M37 36H55M37 44H55M37 50H55M37 56H48" stroke="#fff" stroke-width="2"/>
  </svg>
  <h3>WHAT WE DO</h3>
  <p>Praesent elementum elit at tellus Curabitur metus ipsum luctus eu malesuadFusce tellus Sed metus augue convallis et vehicula ut pulvina</p>
  <div class="btn-outline">LEARN MORE</div>
</div>
<div class="service" style="left:593px">
  <svg class="service-icon" viewBox="0 0 95 95">
    <circle cx="47.5" cy="47.5" r="47.5" fill="var(--accent-blue)"/>
    <g fill="#fff">
      <circle cx="33" cy="36" r="5"/><rect x="27" y="43" width="12" height="20" rx="4"/>
      <circle cx="62" cy="36" r="5"/><rect x="56" y="43" width="12" height="20" rx="4"/>
      <circle cx="47.5" cy="33" r="6"/><rect x="40" y="41" width="15" height="26" rx="5"/>
    </g>
  </svg>
  <h3>OUR PEOPLE</h3>
  <p>Praesent elementum elit at tellus Curabitur metus ipsum luctus eu malesuadFusce tellus Sed metus augue convallis</p>
  <div class="btn-outline">LEARN MORE</div>
</div>
<div class="service" style="left:878px">
  <svg class="service-icon" viewBox="0 0 95 95">
    <circle cx="47.5" cy="47.5" r="47.5" fill="var(--accent-blue)"/>
    <g stroke="#fff" stroke-width="2" fill="none">
      <path d="M47.5 24V66M36 66H59M29 34H66"/>
      <path d="M29 34L22 50M29 34L36 50M66 34L59 50M66 34L73 50"/>
      <path d="M21 50A8 5 0 0 0 37 50Z M58 50A8 5 0 0 0 74 50Z" fill="#fff"/>
    </g>
  </svg>
  <h3>OUR FIRM</h3>
  <p>Praesent elementum elit at tellus Curabitur metus ipsum luctus eu malesuadFusce tellus Sed metus augue convallis et</p>
  <div class="btn-outline">LEARN MORE</div>
</div>

<section class="team">
  <h2 class="team-title">OUR TEAM</h2>
  <div class="team-divider" style="left:400px"></div>
  <div class="team-divider" style="left:603px"></div>
  <div class="team-divider" style="left:806px"></div>
  <div class="member" style="left:300px">
    <div class="member-photo" role="img" aria-label="Portrait of Jonas C. Terholt"></div>
    <h4>Jonas C. Terholt</h4>
    <p>Praesent elementum elit at tellus<br>Curabitur metus ipsum</p>
    <span class="more">READ MORE</span>
  </div>
  <div class="member" style="left:504px">
    <div class="member-photo" role="img" aria-label="Portrait of Lukas Brenner-Aldt"></div>
    <h4>Lukas Brenner-Aldt</h4>
    <p>Praesent elementum elit at tellus<br>Curabitur metus ipsum</p>
    <span class="more">READ MORE</span>
  </div>
  <div class="member" style="left:704px">
    <div class="member-photo" role="img" aria-label="Portrait of Dieter-Paul Ostwald"></div>
    <h4>Dieter-Paul Ostwald</h4>
    <p>Praesent elementum elit at tellus<br>Curabitur metus ipsum</p>
    <span class="more">READ MORE</span>
  </div>
  <div class="member" style="left:908px">
    <div class="member-photo" role="img" aria-label="Portrait of Martin E. Kellberg"></div>
    <h4>Martin E. Kellberg</h4>
    <p>Praesent elementum elit at tellus<br>Curabitur metus ipsum</p>
    <span class="more">READ MORE</span>
  </div>
</section>

<h2 class="news-title">News &amp; Blogs</h2>
<div class="see-all">See All</div>
<article class="post" style="left:185px">
  <div class="post-image" role="img" aria-label="Classical columns of a courthouse" style="background:linear-gradient(180deg,#cfcfcf,#8f8f8f)"></div>
  <h4>Fusce tellus Sed metus augue</h4>
  <p>convallis et vehicula ut pulvinar eu ante Integer<br>orci tellus tristique vitae consequat nec</p>
  <span class="more">READ MORE</span>
</article>
<article class="post" style="left:482px">
  <div class="post-image" role="img" aria-label="Business meeting around a conference table" style="background:linear-gradient(180deg,#7d8a99,#3b3f45)"></div>
  <h4>Donec convallis pede venenatis</h4>
  <p>convallis et vehicula ut pulvinar eu ante Integer orci<br>tellus tristique vitae consequat nec</p>
  <span class="more">READ MORE</span>
</article>
<article class="post" style="left:783px">
  <div class="post-image" role="img" aria-label="Team reviewing documents on a desk" style="background:linear-gradient(180deg,#b9c2cc,#a0856a)"></div>
  <h4>Aliquam erat volutpat</h4>
  <p>convallis et vehicula ut pulvinar eu ante Integer orci<br>tellus tristique vitae consequat nec</p>
  <span class="more">READ MORE</span>
</article>

<footer class="site-footer">
  <div class="footer-nav"><span>HOME</span><span>OUR FIRM</span><span>WHAT WE DO</span><span>OUR PEOPLE</span><span>CONTACT US</span></div>
  <div class="copyright">© 2016 Company Name &nbsp;All right reserved &nbsp;Term of Use</div>
  <div class="social" style="left:183px"></div>
  <div class="social" style="left:217px"></div>
  <div class="social" style="left:249px"></div>
  <address class="address" style="font-style:normal">PRTV Patentanwälte<br>Pahl . Reiner - Tessmann . Vogt<br>Lindenhofweg 12<br>D-80000 Musterstadt</address>
</footer>

</body>
</html>
```